Brisk Tide needs a web page for E-commerce site

Small startup business looking for a custom website for my New Saltwater apparel Co.

COMPANY OVERVIEW

Brisk Tide was founded In Mont Belvieu, Tx, right on the heart of pelham cove.

Brisk Tide is the adrenaline, sweat pumping moment you find yourself setting the hook on a monster fish. This is the moment when all your senses come to life as you work to land that trophy, and after a grueling fight when your hi-fiving your fishing buddies...It's that moment... when the waters and the air around you are Brisk Sweet....All or Nothing...pure Addiction......This is BRISK TIDE

Looking for a sharp clean sexy web page for my ecommerce page

I like the look of black background websites.

www.brisktide-demo.com
Updates

I am using shopvane as my host site if that means anything to y'all

Thank you all for the submissions! There were some great ones!  I will have more projects in the future. thanks again

Target Market(s)

inshore/offshore fishing, saltwater enthusiast

Industry/Entity Type

Business

Requirements
Must have
• logo's

inshore/offshore fishing appeal

compatible with shopvane site

```html
<!DOCTYPE html>
<html lang="en">
<head>
<meta charset="utf-8">
<title>Brisk Tide – Saltwater Apparel</title>
<link href="https://fonts.googleapis.com/css2?family=Bitter:wght@400;700&family=Open+Sans:wght@400;600&family=Raleway:wght@400;700&family=Crete+Round&display=swap" rel="stylesheet">
<style>
:root{
  --page-bg:#262626;
  --page-stripe:#2c2c2c;
  --topbar:#151515;
  --red:#b80d0f;
  --red-bright:#d51417;
  --red-dark:#8e0a0b;
  --orange:#f39c12;
  --orange-dark:#e08200;
  --slider-dark:#2b2b2b;
  --slider-active:#111;
  --white:#ffffff;
  --panel:#f3f3f3;
  --text-dark:#333;
  --text-mid:#555;
  --price:#e58a1f;
  --band:#060606;
}
*{box-sizing:border-box;margin:0;padding:0}
html,body{width:1066px;height:1200px;overflow:hidden}
body{
  position:relative;
  background:var(--page-bg) repeating-linear-gradient(90deg,var(--page-bg) 0 3px,var(--page-stripe) 3px 5px);
  font-family:"Open Sans",sans-serif;color:var(--white);
}
.abs{position:absolute}
.topbar{left:0;top:0;width:1066px;height:25px;background:var(--topbar);border-bottom:1px solid #000}
.topbar-links{right:91px;top:6px;font:600 11px/14px Arial,sans-serif;color:#ddd;word-spacing:1px}
.topbar-links span{margin:0 5px;color:#aaa}
.brand{left:90px;top:54px;font:700 40px/1 "Bitter",serif;color:var(--white);letter-spacing:1px}
.main-nav{top:101px;font:700 13.5px/16px "Raleway",sans-serif;letter-spacing:.5px}
.nav-home{left:529px;color:var(--red-bright)}
.nav-ship{left:636px}
.nav-rss{left:854px}
.nav-sep{top:98px;width:1px;height:22px;background:#555}
.nav-pointer{left:541px;top:131px;width:0;height:0;border:7px solid transparent;border-bottom-color:var(--red);border-top:0}

.banner{left:90px;top:139px;width:884px;height:285px;overflow:hidden}
.banner-photo{left:450px;top:0;width:388px;height:285px;background:linear-gradient(120deg,#e8d0d4 0%,#c89a88 35%,#a05a4a 55%,#e7c070 80%,#d8303a 100%)}
.banner-deal{left:0;top:0;width:600px;height:285px;background:radial-gradient(ellipse at 40% 50%,var(--red-bright),var(--red-dark));clip-path:polygon(0 0,568px 0,473px 285px,0 285px)}
.deal-line1{left:40px;top:30px;font:400 43px/1 "Raleway",sans-serif;letter-spacing:1px}
.deal-line2{left:40px;top:88px;font:700 66px/1 "Raleway",sans-serif;letter-spacing:1px}
.deal-line3{left:38px;top:176px;font:400 32px/38px "Raleway",sans-serif;letter-spacing:.5px}
.slider-nav{left:838px;top:0;width:46px;height:285px}
.slider-arrow{left:0;width:46px;height:48px;background:linear-gradient(var(--orange),var(--orange-dark));display:flex;align-items:center;justify-content:center}
.slider-num{left:0;width:46px;height:48px;background:var(--slider-dark);font:700 19px/48px Arial,sans-serif;text-align:center;border-bottom:1px solid #222}
.slider-num.is-active{background:var(--slider-active)}
.slider-num.is-active::before{content:"";position:absolute;left:-12px;top:12px;border:12px solid transparent;border-right-color:var(--slider-active);border-left:0}

.welcome{left:0;top:452px;width:1066px;text-align:center;font:700 39px/1 "Bitter",serif;letter-spacing:2.5px}
.welcome em{font-style:normal;color:var(--red-bright)}
.intro{left:92px;top:506px;width:882px;text-align:center;font:600 12.6px/19.5px "Open Sans",sans-serif;color:#eee}
.cta{left:404px;top:583px;width:247px;height:45px;border-radius:12px;background:linear-gradient(#fff,#cfcfcf);box-shadow:0 2px 0 #888,0 3px 4px rgba(0,0,0,.5);text-align:center;font:700 22px/45px "Bitter",serif;color:var(--red);letter-spacing:1px}

.products{left:90px;top:657px;width:887px;height:560px;background:var(--panel)}
.products-head{left:0;top:0;width:887px;height:47px;background:linear-gradient(var(--red-bright),var(--red-dark));border-radius:5px 5px 0 0}
.products-title{left:13px;top:11px;font:400 21px/1 "Bitter",serif;letter-spacing:1px}
.pager{top:12px;width:22px;height:21px;background:#fff;border-radius:2px;display:flex;align-items:center;justify-content:center}
.card{top:73px;width:174px}
.card-img{width:174px;height:115px;border:3px solid #e2e2e2;background:linear-gradient(#ececec,#dcdcdc);display:flex;align-items:center;justify-content:center;gap:4px}
.shirt{width:70px;height:82px;border-radius:10px 10px 4px 4px}
.shirt.black{background:linear-gradient(#3a3026,#1f1912)}
.shirt.yellow{background:linear-gradient(#fbf3a0,#eee17a)}
.card-name{margin-top:9px;font:400 11px/16px Arial,sans-serif;color:var(--text-dark)}
.card-buy{margin-top:4px;display:flex;align-items:center;justify-content:space-between}
.price{font:400 16.5px/1 Arial,sans-serif;color:var(--price)}
.add-cart{width:105px;height:28px;border-radius:3px;background:linear-gradient(var(--red-bright),var(--red-dark));display:flex;align-items:center;justify-content:center;gap:6px;font:700 12.5px/1 Arial,sans-serif;color:#fff}

.band-fold{top:947px;width:0;height:0;border-style:solid}
.band{left:60px;top:959px;width:946px;height:169px;background:var(--band);padding:4px}
.band-inner{width:100%;height:100%;border:1px dashed #555;position:relative}
.col-title{font:400 25px/1 "Crete Round",serif}
.col-sep{top:19px;width:1px;height:130px;border-left:1px dashed #444}
.thumb{left:33px;top:55px;width:111px;height:83px;border:3px solid #777;background:linear-gradient(135deg,#9fd3a8,#7cc0c9 50%,#e27b6f)}
.latest-name{left:168px;top:56px;font:400 16.5px/18px "Crete Round",serif;color:#ddd}
.latest-price{left:167px;top:99px;font:400 40px/1 Arial,sans-serif;letter-spacing:-1px}
.mail-label{left:423px;top:60px;font:400 13.5px/1 "Crete Round",serif;color:#ddd}
.mail-input{left:422px;top:71px;width:252px;height:27px;background:#fff;font:400 13.5px/27px "Crete Round",serif;color:#222;padding-left:8px}
.mail-btn{left:422px;top:104px;width:113px;height:31px;background:var(--red-dark);font:400 13.5px/31px "Crete Round",serif;text-align:center}
.cart-count{left:826px;top:75px;font:400 31px/1 "Crete Round",serif}
.cart-count em{font-style:normal;color:var(--red-bright)}
.cart-note{left:765px;top:129px;font:400 13.5px/1 "Crete Round",serif;color:#ddd}

.copyright{left:0;top:1148px;width:1066px;text-align:center;font:400 11px/20px Arial,sans-serif;color:var(--text-mid)}
</style>
</head>
<body>

<div class="abs topbar"></div>
<div class="abs topbar-links">My Account<span>|</span>Order Status<span>|</span>Wish Lists<span>|</span>Gift Certificates<span>|</span>View Cart<span>|</span>Sign in or Create an Account</div>

<div class="abs brand">BRISK TIDE</div>

<div class="abs main-nav nav-home">HOME</div>
<div class="abs nav-sep" style="left:604px"></div>
<div class="abs main-nav nav-ship">SHIPPING &amp; RETURNS</div>
<div class="abs nav-sep" style="left:822px"></div>
<div class="abs main-nav nav-rss">RSS SYNDICATION</div>
<div class="abs nav-pointer"></div>

<section class="abs banner">
  <div class="abs banner-photo" role="img" aria-label="Three smiling shoppers holding colourful shopping bags in front of a sale sign"></div>
  <div class="abs banner-deal">
    <div class="abs deal-line1">DEAL OF THE DAY</div>
    <div class="abs deal-line2">25% OFF</div>
    <div class="abs deal-line3">SELECTED T-SHIRT RANGE<br>TODAY ONLY</div>
  </div>
  <div class="abs slider-nav">
    <div class="abs slider-arrow" style="top:0"><svg width="14" height="8"><path d="M0 8L7 0L14 8Z" fill="#222"/></svg></div>
    <div class="abs slider-num is-active" style="top:48px">1</div>
    <div class="abs slider-num" style="top:96px">2</div>
    <div class="abs slider-num" style="top:144px">3</div>
    <div class="abs slider-num" style="top:190px">4</div>
    <div class="abs slider-arrow" style="top:237px"><svg width="14" height="8"><path d="M0 0L7 8L14 0Z" fill="#222"/></svg></div>
  </div>
</section>

<h1 class="abs welcome">WELCOME TO <em>BRISKTIDE</em></h1>
<p class="abs intro">simply dummy text of the printing and typesetting industry. Lorem Ipsum has been the industry's standard dummy text ever since the 1500s, when an unknown printer took a galley of type and scrambled it to make when an unknown printer took a galley of type and scrambled it to make a type specimen book. It has survived not only five centuries, but also the leap into electronic typesetting, remaining essentially unchanged.</p>
<div class="abs cta">Get Started Now</div>

<div class="abs band-fold" style="left:60px;border-width:12px 30px 0 0;border-color:transparent #111 transparent transparent;top:947px"></div>
<div class="abs band-fold" style="left:976px;border-width:12px 0 0 30px;border-color:transparent transparent transparent #111;top:947px"></div>
<div class="abs band-fold" style="left:60px;border-width:0 30px 12px 0;border-color:transparent #111 transparent transparent;top:1128px"></div>
<div class="abs band-fold" style="left:976px;border-width:0 0 12px 30px;border-color:transparent transparent transparent #111;top:1128px"></div>

<section class="abs products">
  <div class="abs products-head">
    <h2 class="abs products-title">NEW PRODUCTS</h2>
    <div class="abs pager" style="left:818px"><svg width="6" height="9"><path d="M6 0L0 4.5L6 9Z" fill="#b80d0f"/></svg></div>
    <div class="abs pager" style="left:852px"><svg width="6" height="9"><path d="M0 0L6 4.5L0 9Z" fill="#b80d0f"/></svg></div>
  </div>

  <div class="abs card" style="left:27px">
    <div class="card-img" role="img" aria-label="Black t-shirt, back and front"><div class="shirt black"></div><div class="shirt black"></div></div>
    <p class="card-name">Cupidatat non proident, sunt culpa qui officia</p>
    <div class="card-buy"><span class="price">$139.99</span><span class="add-cart"><svg width="18" height="15" viewBox="0 0 18 15"><path d="M5 6L9 1L13 6M1 6H17L15 14H3Z" fill="none" stroke="#fff" stroke-width="1.6"/></svg>Add to Cart</span></div>
  </div>
  <div class="abs card" style="left:247px">
    <div class="card-img" role="img" aria-label="Yellow t-shirt with marlin print, back and front"><div class="shirt yellow"></div><div class="shirt yellow"></div></div>
    <p class="card-name">Cupidatat non proident, sunt culpa qui officia</p>
    <div class="card-buy"><span class="price">$139.99</span><span class="add-cart"><svg width="18" height="15" viewBox="0 0 18 15"><path d="M5 6L9 1L13 6M1 6H17L15 14H3Z" fill="none" stroke="#fff" stroke-width="1.6"/></svg>Add to Cart</span></div>
  </div>
  <div class="abs card" style="left:461px">
    <div class="card-img" role="img" aria-label="Black t-shirt, back and front"><div class="shirt black"></div><div class="shirt black"></div></div>
    <p class="card-name">Cupidatat non proident, sunt culpa qui officia</p>
    <div class="card-buy"><span class="price">$139.99</span><span class="add-cart"><svg width="18" height="15" viewBox="0 0 18 15"><path d="M5 6L9 1L13 6M1 6H17L15 14H3Z" fill="none" stroke="#fff" stroke-width="1.6"/></svg>Add to Cart</span></div>
  </div>
  <div class="abs card" style="left:676px">
    <div class="card-img" role="img" aria-label="Yellow t-shirt with marlin print, back and front"><div class="shirt yellow"></div><div class="shirt yellow"></div></div>
    <p class="card-name">Cupidatat non proident, sunt culpa qui officia</p>
    <div class="card-buy"><span class="price">$139.99</span><span class="add-cart"><svg width="18" height="15" viewBox="0 0 18 15"><path d="M5 6L9 1L13 6M1 6H17L15 14H3Z" fill="none" stroke="#fff" stroke-width="1.6"/></svg>Add to Cart</span></div>
  </div>
</section>

<section class="abs band">
  <div class="band-inner">
    <h3 class="abs col-title" style="left:28px;top:18px">Latest Products</h3>
    <div class="abs thumb" role="img" aria-label="Spool of ribbon printed with cars, helicopters and trucks"></div>
    <div class="abs latest-name">Transport Ribbon - Car,<br>Helicopter &amp; Truck</div>
    <div class="abs latest-price">$2.50</div>

    <div class="abs col-sep" style="left:406px"></div>

    <h3 class="abs col-title" style="left:423px;top:18px">Mailing List</h3>
    <div class="abs mail-label" style="top:60px">Subscribe to our mailing list below:</div>
    <div class="abs mail-input" style="top:76px">Enter Your Email Address</div>
    <div class="abs mail-btn" style="top:109px">Subscribe</div>

    <div class="abs col-sep" style="left:688px"></div>

    <h3 class="abs col-title" style="left:716px;top:18px">Shopping Cart</h3>
    <svg class="abs" style="left:720px;top:68px" width="42" height="46" viewBox="0 0 42 46"><path d="M11 16L21 3L31 16" fill="none" stroke="#fff" stroke-width="3"/><rect x="1" y="15" width="40" height="6" fill="#fff"/><path d="M4 23H38L35 45H7Z" fill="#fff"/><g stroke="#000" stroke-width="1.5"><path d="M10 27V41M14 27V41M18 27V41M22 27V41M26 27V41M30 27V41M34 27V41"/></g></svg>
    <div class="abs cart-count">0 <em>Items</em></div>
    <div class="abs cart-note">Your Cart Is Empty Now!</div>
  </div>
</section>

<footer class="abs copyright">Copyright © 2007 - 2013 - BRISKTIDE &amp; Security, INC. - All Rights Reserved<br>Powered by: brisktide-demo.com and HarborBidList.com</footer>

</body>
</html>
```